Ledgerwise Business Card Design

Business Card Design for new business called Ledgerwise focused on selling business software to small and medium size companies who have outgrown Tallyhouse. Similar companies would be Tallyhouse, Vemo, BrightCore. Also Dealharbor would be good to look at for additional ideas around look and feel.

Target Market(s)

Business to Business

Industry/Entity Type

Information Technology

Contact Information for Business Card

Standard Business Card Information

Font styles to use
Sans Serif

```html
<!DOCTYPE html>
<html lang="en">
<head>
<meta charset="utf-8">
<title>Ledgerwise Business Card</title>
<link rel="stylesheet" href="https://fonts.googleapis.com/css2?family=Open+Sans:wght@400;600;700&display=swap">
<style>
  :root {
    --orange: #ff8200;
    --navy: #1b4f86;
    --white: #ffffff;
    --backdrop: #ecebe9;
  }
  * { margin: 0; padding: 0; box-sizing: border-box; }
  html, body { width: 1200px; height: 900px; overflow: hidden; }
  body {
    position: relative;
    background: var(--backdrop);
    font-family: "Open Sans", Arial, sans-serif;
  }
  .card {
    position: absolute;
    border-radius: 18px;
    overflow: hidden;
    box-shadow: 0 6px 18px rgba(0,0,0,0.12);
  }
  .card-front { left: 78px; top: 35px; width: 588px; height: 363px; background: var(--white); }
  .card-back { left: 390px; top: 506px; width: 565px; height: 350px; background: var(--orange); }

  .accent-bar { position: absolute; width: 11px; }
  .accent-bar.orange { left: 0; top: 68px; height: 218px; background: var(--orange); }
  .accent-bar.navy { right: 0; top: 194px; height: 123px; background: var(--navy); }

  .holder { position: absolute; left: 44px; top: 64px; }
  .holder-name { color: var(--orange); font-weight: 600; font-size: 20px; line-height: 26px; }
  .holder-title { color: var(--navy); font-size: 15px; line-height: 20px; }

  .address { position: absolute; left: 44px; top: 132px; color: var(--navy); font-size: 15px; line-height: 18px; }

  .contacts { position: absolute; left: 44px; top: 191px; list-style: none; }
  .contacts li { display: flex; align-items: center; height: 24.5px; color: var(--navy); font-size: 15px; }
  .contacts svg { width: 13px; height: 13px; margin-right: 10px; fill: var(--orange); }

  .brand { position: absolute; display: flex; align-items: center; font-weight: 700; letter-spacing: 0.5px; }
  .brand-dot { border-radius: 50%; flex: none; }
  .card-front .brand { left: 286px; top: 228px; color: var(--navy); font-size: 36px; }
  .card-front .brand-dot { width: 22px; height: 22px; background: var(--navy); margin-right: 12px; }
  .card-back .brand { left: 0; right: 0; top: 148px; justify-content: center; color: var(--white); font-size: 40px; }
  .card-back .brand-dot { width: 24px; height: 24px; background: var(--white); margin-right: 14px; }

  .back-web { position: absolute; left: 0; right: 0; top: 286px; text-align: center; color: var(--white); font-weight: 700; font-size: 13px; }
</style>
</head>
<body>
  <section class="card card-front">
    <div class="accent-bar orange"></div>
    <div class="accent-bar navy"></div>
    <div class="holder">
      <p class="holder-name">Marcus Hale</p>
      <p class="holder-title">Managing Director</p>
    </div>
    <p class="address">12345, Address Goes Here<br>Country Name, 123456</p>
    <ul class="contacts">
      <li><svg viewBox="0 0 16 16"><path d="M3.5 1l3 3-1.6 1.8a9 9 0 0 0 5.3 5.3L12 9.5l3 3-1.8 2.2C7.5 15 1 8.5 1.3 2.8z"/></svg>(044)-456-7890</li>
      <li><svg viewBox="0 0 16 16"><path d="M4 1h8v4H4z M1 6h14v7h-3v2H4v-2H1z M5 10v4h6v-4z" fill-rule="evenodd"/></svg>123-456-7890</li>
      <li><svg viewBox="0 0 16 16"><path d="M1 3h14v1.5L8 9 1 4.5z M1 6l7 4.5L15 6v7H1z"/></svg>info@youremail.com</li>
      <li><svg viewBox="0 0 16 16"><path d="M6.5 9.5l3-3M7 4l1.5-1.5a3 3 0 0 1 4.5 4.5L11.5 8.5M9 12l-1.5 1.5A3 3 0 0 1 3 9l1.5-1.5" fill="none" stroke="#ff8200" stroke-width="1.8" stroke-linecap="round"/></svg>www.website.com</li>
    </ul>
    <div class="brand"><span class="brand-dot"></span>Ledgerwise</div>
  </section>

  <section class="card card-back">
    <div class="brand"><span class="brand-dot"></span>Ledgerwise</div>
    <p class="back-web">www.website.com</p>
  </section>
</body>
</html>
```